Business Card for Makeup Artist

I need a business card designed for my makeup and hair artistry business which is primarily events and weddings focused. The card needs to be sleek, simple, stylish and appealing to women. I would prefer a white background but open to suggestions also. I also love the marble background look. I have attached some example pics. It needs to be a double sided card with logo and/or design on one side and contact details in the centre of the card on the other side. NO LOGO ON BACK. Examples attached.

Target Market(s)

Females age 14-55

Industry/Entity Type

Business

Contact Information for Business Card

Nora Pelling
Principal Makeup Artist
P: 0412 903 251
E: nora@lumivamakeup.com.au
W: www.lumivamakeup.com.au

Requirements
Should not have
• No yellow, green, red or blue in the design.

```html
<!DOCTYPE html>
<html lang="en">
<head>
<meta charset="utf-8">
<title>Lumiva Makeup Artistry – Business Card</title>
<link rel="stylesheet" href="https://fonts.googleapis.com/css2?family=Arimo:wght@400;700&display=swap">
<style>
  :root {
    --page: #1d1d1f;
    --card-black: #000000;
    --orchid: #bf75a0;
    --white: #ffffff;
    --soft-white: #e9e9e9;
    --photo-dark: #1a1416;
    --photo-skin: #d9b3a5;
    --photo-rose: #b8467a;
    --rule: #8a8a8a;
  }
  * { margin: 0; padding: 0; box-sizing: border-box; }
  html, body {
    width: 1200px; height: 800px; overflow: hidden;
    background: var(--page);
    font-family: "Arimo", Arial, sans-serif;
  }
  .canvas { position: relative; width: 1200px; height: 800px; }

  .card {
    position: absolute; top: 238px;
    width: 535px; height: 306px;
    background: var(--card-black);
    overflow: hidden;
    box-shadow: 0 4px 14px rgba(0,0,0,0.6);
  }
  .card--front { left: 50px; }
  .card--back { left: 618px; }

  .card__art { position: absolute; inset: 0; }

  .brand { position: absolute; left: 44px; top: 30px; color: var(--white); }
  .brand__name {
    display: block; font-size: 60px; font-weight: 400;
    letter-spacing: 1px; line-height: 1;
  }
  .brand__tagline {
    display: block; font-size: 17px; color: var(--soft-white);
    letter-spacing: 0.5px; line-height: 1; margin: 6px 0 0 56px;
  }

  .contact {
    position: absolute; left: 0; right: 0; top: 58px;
    text-align: center; color: var(--white);
  }
  .contact__name { font-size: 26px; line-height: 1; }
  .contact__role { font-size: 14px; margin-top: 10px; color: var(--orchid); letter-spacing: 0.5px; }
  .contact__list {
    list-style: none; margin-top: 26px;
    display: flex; flex-direction: column; align-items: center; gap: 8px;
  }
  .contact__item {
    display: flex; align-items: center; gap: 8px;
    font-size: 13px; line-height: 1;
  }
  .contact__icon { width: 13px; height: 13px; flex: none; }

  .web-line {
    position: absolute; left: 66px; right: 72px; top: 252px;
    display: flex; align-items: center; gap: 14px;
    color: var(--soft-white); font-size: 13px;
  }
  .web-line__rule { flex: 1; height: 1px; background: var(--rule); }
</style>
</head>
<body>
<main class="canvas">

  <section class="card card--front">
    <svg class="card__art" width="535" height="306" viewBox="0 0 535 306">
      <defs>
        <linearGradient id="portrait-tone" x1="0" y1="0" x2="1" y2="1">
          <stop offset="0" stop-color="var(--photo-dark)"/>
          <stop offset="0.45" stop-color="var(--photo-skin)"/>
          <stop offset="0.8" stop-color="var(--photo-rose)"/>
          <stop offset="1" stop-color="var(--photo-dark)"/>
        </linearGradient>
      </defs>
      <rect x="382" y="0" width="153" height="236" fill="url(#portrait-tone)"
            role="img" aria-label="Beauty portrait photo of a model with glamour makeup and pink flowers in her hair"/>
      <polygon points="0,106 392,246 535,194 535,306 0,306" fill="var(--orchid)"/>
      <polyline points="0,106 392,246 535,194" fill="none" stroke="var(--white)" stroke-width="1.5"/>
    </svg>

    <div class="brand">
      <span class="brand__name">Lumiva</span>
      <span class="brand__tagline">MAKEUP ARTISTRY</span>
    </div>
  </section>

  <section class="card card--back">
    <div class="contact">
      <p class="contact__name">Nora Pelling</p>
      <p class="contact__role">Principal Makeup Artist</p>
      <ul class="contact__list">
        <li class="contact__item">
          <svg class="contact__icon" viewBox="0 0 13 13"><rect width="13" height="13" rx="2" fill="var(--white)"/><path d="M4 3 L5.5 3 L6 5 L5 5.8 Q6 7.8 7.4 8.3 L8.2 7.3 L10 8 L10 9.6 Q6 10.2 3.5 5 Z" fill="var(--orchid)"/></svg>
          <span>0412 903 251</span>
        </li>
        <li class="contact__item">
          <svg class="contact__icon" viewBox="0 0 13 13"><rect width="13" height="13" rx="2" fill="var(--white)"/><rect x="2.5" y="4" width="8" height="5.5" fill="none" stroke="var(--orchid)"/><path d="M2.5 4 L6.5 7 L10.5 4" fill="none" stroke="var(--orchid)"/></svg>
          <span>nora@lumivamakeup.com.au</span>
        </li>
      </ul>
    </div>
    <div class="web-line">
      <span class="web-line__rule"></span>
      <span>www.lumivamakeup.com.au</span>
      <span class="web-line__rule"></span>
    </div>
  </section>

</main>
</body>
</html>
```